Craft oriented film company needs a Business Card design

Hi all,
We're a 2-man band film company in New Zealand called Brindle Pictures. We're good honest blokes, who are very passionate about the craft of film making. I've attached our current logo which has a bit of a crafty/artisan feel that we like. Feel free to use it - or throw the baby out with the bathwater and start again..... you never know, you might inspire a complete brand re-work.

In any case, the vibe we want to give out is that we are solid, dependable and no bullshit - but without compromising creative excellence and being in the now. We like the 'Brooklyn' artisan style of work.

Preferably single sided.

We need the standard stuff:
Name, job title, cellphone, email address and physical address (this can be smaller if you like - street, suburb, city & zip, country [if you want])

Check out our website to learn more about us: brindlepictures.example

Target Market(s)

Brand marketers and advertising agency creatives looking for video production.

Requirements
Should not have
• Nothing flashy or too 'futuristic', we want it to feel grounded and real. A limited colour palette is preferred.
We don't want any film reels or cameras or anything obvious like that.

```html
<!DOCTYPE html>
<html lang="en">
<head>
<meta charset="utf-8">
<title>Brindle Pictures — Business Card</title>
<link rel="stylesheet" href="https://fonts.googleapis.com/css2?family=Open+Sans:wght@400;600&display=swap">
<style>
  :root {
    --backdrop: #7d6a52;
    --card-white: #f7f7f7;
    --card-shade: #e6e6e6;
    --ink: #111214;
    --silver: #b9b9b9;
    --text-dark: #2b2b2b;
    --text-mid: #555555;
  }
  html, body {
    margin: 0;
    width: 1200px;
    height: 1023px;
    overflow: hidden;
    background: var(--backdrop);
    font-family: "Open Sans", Arial, sans-serif;
  }
  .card {
    position: absolute;
    left: 180px;
    top: 271px;
    width: 840px;
    height: 480px;
    box-shadow: 0 18px 40px rgba(0,0,0,0.35);
    overflow: hidden;
  }
  .card-art { position: absolute; inset: 0; }
  .brand-mark {
    position: absolute;
    left: 225px;
    top: 110px;
    width: 210px;
    height: 210px;
    display: flex;
    align-items: center;
    justify-content: center;
    text-align: center;
    color: var(--card-white);
    font-weight: 600;
    font-size: 27px;
    line-height: 1.15;
    text-transform: uppercase;
    letter-spacing: 1px;
  }
  .holder {
    position: absolute;
    right: 70px;
    top: 48px;
    text-align: right;
  }
  .holder-name {
    margin: 0;
    font-weight: 400;
    font-size: 28px;
    color: var(--text-dark);
    letter-spacing: 0.5px;
  }
  .holder-role {
    margin: 2px 0 0;
    font-size: 14px;
    color: var(--text-mid);
  }
  .address {
    position: absolute;
    right: 70px;
    top: 168px;
    margin: 0;
    text-align: right;
    font-style: normal;
    font-size: 17px;
    line-height: 1.4;
    color: var(--text-dark);
  }
  .contacts {
    position: absolute;
    right: 40px;
    top: 318px;
    margin: 0;
    padding: 0;
    list-style: none;
    text-align: right;
    font-size: 16px;
    line-height: 31px;
    color: var(--text-dark);
  }
  .contacts li { display: flex; justify-content: flex-end; align-items: center; gap: 8px; }
  .contacts svg { width: 16px; height: 16px; flex: none; }
</style>
</head>
<body>
  <div class="card">
    <svg class="card-art" viewBox="0 0 840 480" width="840" height="480" aria-hidden="true">
      <defs>
        <linearGradient id="face" x1="0" y1="0" x2="1" y2="1">
          <stop offset="0" stop-color="var(--card-white)"/>
          <stop offset="1" stop-color="var(--card-shade)"/>
        </linearGradient>
      </defs>
      <rect class="ink-field" width="840" height="480" fill="var(--ink)"/>
      <path class="silver-arc" d="M215 0 C105 80 95 300 245 385 C365 445 510 470 640 480 L840 480 L840 0 Z" fill="var(--silver)"/>
      <path class="white-face" d="M240 0 C135 85 130 290 275 375 C395 440 535 466 665 480 L840 480 L840 0 Z" fill="url(#face)"/>
      <circle class="brand-disc" cx="330" cy="215" r="108" fill="var(--ink)"/>
    </svg>

    <div class="brand-mark">Brindle<br>Pictures</div>

    <div class="holder">
      <p class="holder-name">MARK DALTON</p>
      <p class="holder-role">Director</p>
    </div>

    <address class="address">418 Harbour View Rd, Unit B<br>Northcote, Auckland 0627</address>

    <ul class="contacts">
      <li>+64-21-55-0147
        <svg viewBox="0 0 16 16"><rect x="4" y="1" width="8" height="14" rx="1.5" fill="none" stroke="#333" stroke-width="1.5"/><line x1="7" y1="12.5" x2="9" y2="12.5" stroke="#333" stroke-width="1.2"/></svg>
      </li>
      <li>info@brindlepictures.example
        <svg viewBox="0 0 16 16"><rect x="1" y="3" width="14" height="10" fill="#333"/><path d="M1 3 L8 9 L15 3" fill="none" stroke="#f7f7f7" stroke-width="1.2"/></svg>
      </li>
      <li>www.brindlepictures.example
        <svg viewBox="0 0 16 16"><circle cx="8" cy="8" r="7" fill="#333"/><path d="M1 8 H15 M8 1 C4 5 4 11 8 15 M8 1 C12 5 12 11 8 15" fill="none" stroke="#f7f7f7" stroke-width="1"/></svg>
      </li>
    </ul>
  </div>
</body>
</html>
```